Letterhead - Quarrington Law Group

I receive a fantastic logo from you guys and I'd like to incorporate it into business cards and letterhead. I accidentally approved design No. 32361474 and contacted designer Ravindra, and Ravindra sent me the zip folder for Design No. 32361417, which I very much appreciate.
I'd like to order business cards and letterhead with Design No. 32361417 as soon as possible, but I want to make sure that you incorporate the correct design (attached). I'd also like to provide my information to add (address, phone number, email, fax) but I'm not quite sure how to do it.
The information that I would like on the business cards and letterhead is as follows:
Quarrington Law Group
Theodore K. Quarrington, Esq.
2741 Hollis Avenue, Suite 520
San Francisco, CA 94087
Office: (415) 378-6130
Fax: (415) 746-0183
ted@quarringtonlawgroup-example.com
Thanks in advance for any guidance.
Ted Quarrington
Quarrington Law Group
(415) 831-4497 (cell)

```html
<!DOCTYPE html>
<html lang="en">
<head>
<meta charset="utf-8">
<title>Quarrington Law Group — Letterhead</title>
<link rel="stylesheet" href="https://fonts.googleapis.com/css2?family=Lato:wght@400;700&family=Montserrat:wght@400&display=swap">
<style>
  :root {
    --backdrop: #e9e7e4;
    --paper: #ffffff;
    --ink: #1c1c1c;
    --brand-blue: #0a8fcb;
    --footer-text: #ffffff;
  }
  * { box-sizing: border-box; margin: 0; padding: 0; }
  html, body {
    width: 1200px;
    height: 1141px;
    overflow: hidden;
    background: var(--backdrop);
  }
  .letterhead {
    position: absolute;
    left: 210px;
    top: 20px;
    width: 779px;
    height: 1100px;
    background: var(--paper);
    box-shadow: 0 2px 10px rgba(0,0,0,0.18);
    overflow: hidden;
    font-family: "Lato", sans-serif;
    color: var(--ink);
  }
  .brand {
    position: absolute;
    left: 38px;
    top: 100px;
    display: flex;
    align-items: center;
    gap: 12px;
  }
  .brand-square {
    width: 22px;
    height: 22px;
    background: var(--brand-blue);
  }
  .brand-name {
    font-weight: 700;
    font-size: 30px;
    letter-spacing: 0.5px;
    color: var(--ink);
  }
  .letter {
    position: absolute;
    left: 39px;
    top: 280px;
    width: 701px;
    font-size: 15.5px;
    line-height: 18.5px;
  }
  .letter-date { font-size: 16px; margin-bottom: 19px; }
  .recipient { margin-bottom: 17px; }
  .salutation {
    font-weight: 700;
    font-size: 20px;
    margin: 14px 0 23px;
  }
  .letter-body p {
    text-align: justify;
    line-height: 17px;
    margin-bottom: 18px;
    letter-spacing: 0.15px;
  }
  .closing { margin-top: 40px; }
  .footer-band {
    position: absolute;
    left: 0;
    bottom: 0;
    width: 779px;
    height: 216px;
  }
  .footer-contact {
    position: absolute;
    left: 41px;
    top: 946px;
    font-family: "Montserrat", sans-serif;
    font-weight: 400;
    font-size: 12.5px;
    line-height: 15.8px;
    color: var(--footer-text);
  }
  .footer-address { margin-bottom: 10px; font-style: normal; }
  .contact-line { display: flex; align-items: center; gap: 6px; }
  .contact-icon { width: 10px; height: 10px; flex: none; }
</style>
</head>
<body>
  <main class="letterhead">
    <header class="brand">
      <span class="brand-square"></span>
      <span class="brand-name">Quarrington Law Group</span>
    </header>

    <section class="letter">
      <p class="letter-date">January-03-2020</p>
      <p class="recipient">Mr, John Doe<br>President</p>
      <p class="recipient">Link Corpporation<br>123 Street Name, Suite# 10<br>City, State, 120023</p>
      <p class="salutation">Dear Mr, John</p>
      <div class="letter-body">
        <p>Lorem ipsum dolor sit amet, consectetur adipiscing elit, sed do eiusmod tempor incididunt ut labore et dolore magna aliqua. Ut enim ad minim veniam, quis nostrud exercitation ullamco laboris nisi ut aliquip ex ea commodo consequat. Duis aute irure dolor in reprehenderit in voluptate velit esse cillum dolore eu fugiat nulla pariatur.</p>
        <p>Lorem ipsum dolor sit amet, consectetur adipiscing elit, sed do eiusmod tempor incididunt ut labore et dolore magna aliqua. Ut enim ad minim veniam, quis nostrud exercitation ullamco laboris nisi ut aliquip ex ea commodo consequat. Duis aute irure dolor in reprehenderit in voluptate velit esse cillum dolore eu fugiat nulla pariatur.</p>
        <p>Lorem ipsum dolor sit amet, consectetur adipiscing elit, sed do eiusmod tempor incididunt ut labore et dolore magna aliqua. Ut enim ad minim veniam, quis nostrud exercitation ullamco laboris nisi ut aliquip ex ea commodo consequat.</p>
        <p>Excepteur sint occaecat cupidatat non proident, sunt in culpa qui officia deserunt mollit anim id est laborum. re et dolore magnam aliquam quaerat voluptatem.</p>
      </div>
      <p class="closing">Regards</p>
    </section>

    <svg class="footer-band" viewBox="0 0 779 216" preserveAspectRatio="none" role="img" aria-label="Blue footer band with a soft curved top edge">
      <path fill="var(--brand-blue)" d="M0,62 C260,20 520,150 779,100 L779,216 L0,216 Z"/>
    </svg>

    <footer class="footer-contact">
      <address class="footer-address">
        Quarrington Law Group<br>
        Theodore K. Quarrington, Esq.<br>
        2741 Hollis Avenue, Suite 520<br>
        San Francisco, CA 94087
      </address>
      <div class="contact-line">
        <svg class="contact-icon" viewBox="0 0 10 10"><path fill="#fff" d="M1,4 C1,1.5 9,1.5 9,4 L7,4.5 L6.5,3.5 L3.5,3.5 L3,4.5 Z M2,5 L8,5 L8.5,9 L1.5,9 Z"/></svg>
        <span>(415) 378-6130</span>
      </div>
      <div class="contact-line">
        <svg class="contact-icon" viewBox="0 0 10 10"><rect x="2.5" y="1" width="5" height="3" fill="#fff"/><rect x="1" y="4" width="8" height="5" fill="#fff"/><rect x="3" y="6" width="4" height="1" fill="var(--brand-blue)"/></svg>
        <span>(415) 746-0183</span>
      </div>
      <div class="contact-line">
        <svg class="contact-icon" viewBox="0 0 10 10"><rect x="2.5" y="0.5" width="5" height="9" rx="1" fill="none" stroke="#fff" stroke-width="1.2"/><circle cx="5" cy="8" r="0.7" fill="#fff"/></svg>
        <span>(415) 831-4497</span>
      </div>
      <div class="contact-line">
        <svg class="contact-icon" viewBox="0 0 10 10"><rect x="0.5" y="2" width="9" height="6.5" fill="#fff"/><path d="M0.5,2 L5,5.8 L9.5,2" fill="none" stroke="var(--brand-blue)" stroke-width="0.9"/></svg>
        <span>ted@quarringtonlawgroup-example.com</span>
      </div>
    </footer>
  </main>
</body>
</html>
```